PineCrest Gate
business card and stationary?
I need double sided standard sized Business Card [3.5" x 2"]
use something easy to read and professional
Professional
Colin Dawlish
Owner
24681 K St
PO Box 517264
Omaha, NE 68247
Colin@PineCrestGate.com
PineCrestGate.com
We Promise Satisfaction!
Custom garage doors built for you!
Longer lasting Torsion springs!
HoistWell Openers
Brookvale and Garvey Doors

```html
<!DOCTYPE html>
<html lang="en">
<head>
<meta charset="utf-8">
<title>PineCrest Gate – Business Card</title>
<link href="https://fonts.googleapis.com/css2?family=Open+Sans:wght@400;600;700&display=swap" rel="stylesheet">
<style>
  :root {
    --page-bg: #e9e6e1;
    --card-black: #1d1d1f;
    --card-black-soft: #2a2a2d;
    --brand-blue: #2a9fd6;
    --brand-blue-deep: #0f6fa3;
    --silver: #c9ccd0;
    --text-light: #e8e8e8;
    --text-muted: #bfc3c7;
  }
  * { margin: 0; padding: 0; box-sizing: border-box; }
  html, body {
    width: 1200px; height: 780px; overflow: hidden;
    background: var(--page-bg);
    font-family: "Open Sans", Arial, sans-serif;
  }
  .card {
    position: absolute; left: 100px; top: 104px;
    width: 1000px; height: 572px;
    border-radius: 30px; overflow: hidden;
    background: radial-gradient(ellipse at 50% 30%, var(--card-black-soft), var(--card-black) 70%);
    box-shadow: 0 10px 30px rgba(0,0,0,0.25);
  }
  .card-band { position: absolute; left: 0; top: 0; width: 1000px; height: 572px; }
  .brand {
    position: absolute; top: 120px; left: 0; width: 100%;
    display: flex; justify-content: center; align-items: center; gap: 18px;
  }
  .brand-dot {
    width: 46px; height: 46px; border-radius: 50%;
    background: var(--brand-blue);
  }
  .brand-name {
    font-size: 56px; font-weight: 700; color: var(--brand-blue);
    letter-spacing: 1px; line-height: 1;
  }
  .brand-rule {
    position: absolute; top: 205px; left: 360px; width: 300px; height: 2px;
    background: var(--silver);
  }
  .identity {
    position: absolute; top: 280px; right: 530px; text-align: right;
  }
  .person-name { font-size: 30px; font-weight: 700; color: var(--brand-blue); line-height: 1.15; }
  .person-role { font-size: 21px; color: var(--text-light); margin-top: 2px; }
  .address { margin-top: 34px; font-size: 20px; color: var(--text-light); line-height: 1.4; }
  .divider {
    position: absolute; left: 500px; top: 282px; width: 2px; height: 150px;
    background: linear-gradient(var(--silver), rgba(201,204,208,0.2));
  }
  .contacts {
    position: absolute; left: 528px; top: 282px; list-style: none;
  }
  .contacts li {
    display: flex; align-items: center; gap: 12px;
    font-size: 20px; color: var(--text-light); height: 36px;
  }
  .contacts svg { width: 22px; height: 22px; flex: none; }
  .website {
    position: absolute; left: 0; bottom: 26px; width: 100%; text-align: center;
    font-size: 22px; font-weight: 600; color: #ffffff; letter-spacing: 1px;
  }
</style>
</head>
<body>
<main class="card">
  <svg class="card-band" viewBox="0 0 1000 572" aria-hidden="true">
    <defs>
      <linearGradient id="bandFill" x1="0" y1="0" x2="0" y2="1">
        <stop offset="0" stop-color="#3db3ea"/>
        <stop offset="1" stop-color="#0f6fa3"/>
      </linearGradient>
    </defs>
    <path d="M0 478 Q500 440 1000 448 L1000 572 L0 572 Z" fill="#d6d9dc"/>
    <path d="M0 486 Q500 452 1000 458 L1000 572 L0 572 Z" fill="url(#bandFill)"/>
  </svg>

  <div class="brand">
    <span class="brand-dot"></span>
    <span class="brand-name">PineCrest Gate</span>
  </div>
  <div class="brand-rule"></div>

  <section class="identity">
    <p class="person-name">Colin Dawlish</p>
    <p class="person-role">Owner</p>
    <p class="address">24681 K St, PO Box 517264<br>Omaha, NE 68247</p>
  </section>

  <div class="divider"></div>

  <ul class="contacts">
    <li>
      <svg viewBox="0 0 24 24"><path d="M6 3l3 0 1.5 5-2 1.5a11 11 0 0 0 6 6l1.5-2 5 1.5v3a2 2 0 0 1-2 2A17 17 0 0 1 4 5a2 2 0 0 1 2-2z" fill="var(--brand-blue)"/></svg>
      402 555-0147
    </li>
    <li>
      <svg viewBox="0 0 24 24"><rect x="7" y="2" width="10" height="20" rx="2" fill="var(--brand-blue)"/><rect x="9" y="5" width="6" height="11" fill="var(--card-black)"/></svg>
      402 555-0182
    </li>
    <li>
      <svg viewBox="0 0 24 24"><rect x="7" y="3" width="10" height="7" fill="var(--brand-blue)"/><rect x="3" y="9" width="18" height="10" rx="2" fill="var(--brand-blue)"/><rect x="7" y="15" width="10" height="6" fill="var(--text-light)"/></svg>
      402 555-0163
    </li>
    <li>
      <svg viewBox="0 0 24 24"><rect x="2" y="5" width="20" height="14" rx="2" fill="var(--brand-blue)"/><path d="M3 6l9 7 9-7" fill="none" stroke="var(--card-black)" stroke-width="2"/></svg>
      Colin@PineCrestGate.com
    </li>
  </ul>

  <p class="website">www.PineCrestGate.com</p>
</main>
</body>
</html>
```